Create a cover for English Grammar Workbook

This book describes a system to learn English in a proper way - we call it The ''Keystone Loop'' System.

It focuses on not only teaching grammar and its structures, but also giving students tips on how to use it and the best ways to remember what they learn.

The cover should have 3 realistic pillars (3D), with one closer to the front to show that this book is the 1st (front) Pillar.

The title is: "Unlocking Tricky Syntax Rules: *A Calm Path toward Fluency"*

Author's name: Dorian Pell

```html
<!DOCTYPE html>
<html lang="en">
<head>
<meta charset="utf-8">
<title>Unlocking Tricky Syntax Rules – Cover</title>
<link rel="stylesheet" href="https://fonts.googleapis.com/css2?family=Roboto+Condensed:ital,wght@0,400;0,500;0,700;1,700&family=Montserrat:wght@600&display=swap">
<style>
  :root {
    --backdrop: #e6e6e6;
    --cover-red: #d2181d;
    --cover-red-deep: #b51217;
    --paper-white: #ffffff;
    --ink-dark: #1d1d1d;
    --pillar-ivory: #efe9df;
    --pillar-gold: #d9b24a;
  }
  * { margin: 0; padding: 0; box-sizing: border-box; }
  html, body {
    width: 1200px;
    height: 800px;
    overflow: hidden;
    background: var(--backdrop);
  }
  .canvas {
    position: relative;
    width: 1200px;
    height: 800px;
  }
  .cover {
    position: absolute;
    left: 345px;
    top: 40px;
    width: 510px;
    height: 720px;
    background: var(--cover-red);
    overflow: hidden;
    color: var(--paper-white);
    font-family: "Roboto Condensed", "Arial Narrow", sans-serif;
  }
  .corner-ribbon {
    position: absolute;
    top: 34px;
    right: -58px;
    width: 240px;
    height: 46px;
    background: var(--paper-white);
    color: var(--cover-red);
    transform: rotate(45deg);
    text-align: center;
    font-weight: 700;
    font-size: 22px;
    line-height: 46px;
    letter-spacing: 0.5px;
  }
  .title {
    position: absolute;
    left: 0;
    right: 0;
    top: 44px;
    text-align: center;
    text-transform: uppercase;
  }
  .title-lead {
    display: block;
    font-weight: 500;
    font-size: 36px;
    line-height: 40px;
  }
  .title-main {
    display: block;
    font-weight: 700;
    font-size: 70px;
    line-height: 68px;
    letter-spacing: 1px;
  }
  .subtitle {
    position: absolute;
    left: 75px;
    top: 229px;
    width: 402px;
    height: 40px;
    background: var(--paper-white);
    color: var(--ink-dark);
    text-align: center;
    font-weight: 700;
    font-style: italic;
    font-size: 24px;
    line-height: 40px;
    text-transform: uppercase;
  }
  .pillars-art {
    position: absolute;
    left: 120px;
    top: 262px;
    width: 270px;
    height: 360px;
    border-radius: 4px;
    background: linear-gradient(180deg, var(--pillar-gold) 0%, var(--pillar-ivory) 14%, var(--pillar-ivory) 86%, var(--pillar-gold) 100%);
    opacity: 0.92;
  }
  .base-rule {
    position: absolute;
    left: 0;
    right: 0;
    top: 622px;
    height: 10px;
    background: var(--paper-white);
  }
  .author {
    position: absolute;
    left: 0;
    right: 0;
    top: 656px;
    text-align: center;
    font-family: "Montserrat", "Helvetica", sans-serif;
    font-weight: 600;
    font-size: 20px;
    letter-spacing: 6px;
    text-transform: uppercase;
  }
</style>
</head>
<body>
  <main class="canvas">
    <section class="cover">
      <div class="corner-ribbon">Easy Guide</div>
      <h1 class="title">
        <span class="title-lead">Unlocking Tricky</span>
        <span class="title-main">Syntax</span>
        <span class="title-main">Rules</span>
      </h1>
      <p class="subtitle">A Calm Path toward Fluency</p>
      <div class="pillars-art" role="img" aria-label="Three white classical pillars with gold capitals and bases, the middle one taller and set forward"></div>
      <div class="base-rule"></div>
      <p class="author">Dorian Pell</p>
    </section>
  </main>
</body>
</html>
```